Meridian Rest Supply Needs Business Card

Looking for a very nice looking business card. Creative but not extravagant. We sell beds and pillows across the U.S. and need something professional but catchy. I have attached the logo.

Name : Dale Fenwick
Title : President
Phone : (800) 417-2964
Email: sleep@quorvana.com
Website: www.quorvana.com

Can be single-sided or double-sided
horizontal or vertical

Can use Blues/Greys

Target Market(s)

Mass Market

Industry/Entity Type

Retail

Contact Information for Business Card

Name : Dale Fenwick
Title : President
Phone : (800) 417-2964
Email: sleep@quorvana.com
Website: www.quorvana.com

Requirements
Must have
• Clean, Modern, Smooth
• Can use Blues/Greys
• On the other side without the information - have something simple like www.quorvana.com or our logo
Nice to have
• Surprise me
Should not have
• Nothing crazy, nothing cluttered

```html
<!DOCTYPE html>
<html lang="en">
<head>
<meta charset="utf-8">
<title>Meridian Rest Supply – Business Card</title>
<link rel="stylesheet" href="https://fonts.googleapis.com/css2?family=Quicksand:wght@300;400;600;700&display=swap">
<style>
  :root {
    --backdrop: #1d1d1e;
    --brand-blue: #33a3d6;
    --brand-blue-deep: #2b93c4;
    --card-grey-light: #767779;
    --card-grey-dark: #5b5c5e;
    --text-light: #e9ecee;
    --text-soft: #d2d5d8;
    --white: #ffffff;
  }
  * { margin: 0; padding: 0; box-sizing: border-box; }
  html, body {
    width: 1200px;
    height: 960px;
    overflow: hidden;
    background: var(--backdrop);
    font-family: "Quicksand", sans-serif;
  }
  .canvas {
    position: relative;
    width: 1200px;
    height: 960px;
  }
  .card {
    position: absolute;
    left: 232px;
    width: 736px;
    height: 420px;
    overflow: hidden;
  }
  /* Information side */
  .card--info {
    top: 50px;
    background: linear-gradient(160deg, var(--card-grey-light) 0%, var(--card-grey-dark) 100%);
  }
  .ribbon {
    position: absolute;
    left: 0;
    top: 92px;
    width: 350px;
    height: 66px;
  }
  .ribbon svg { display: block; }
  .holder {
    position: absolute;
    left: 62px;
    top: 98px;
    color: var(--white);
    line-height: 1.1;
  }
  .holder__name {
    font-weight: 700;
    font-size: 25px;
    letter-spacing: 0.2px;
  }
  .holder__title {
    font-weight: 400;
    font-size: 19px;
    color: var(--text-light);
  }
  .contact {
    position: absolute;
    left: 28px;
    top: 182px;
    list-style: none;
  }
  .contact__item {
    display: flex;
    align-items: center;
    gap: 14px;
    height: 27px;
    font-size: 19px;
    font-weight: 400;
    color: var(--text-soft);
  }
  .contact__icon {
    width: 18px;
    height: 18px;
    flex: none;
  }
  .card__wordmark {
    position: absolute;
    right: 62px;
    top: 170px;
    font-weight: 300;
    font-size: 64px;
    letter-spacing: 2px;
    color: var(--brand-blue);
  }
  .edge-tab {
    position: absolute;
    right: 0;
    top: 262px;
    width: 20px;
    height: 58px;
    background: var(--brand-blue);
  }
  /* Logo side */
  .card--logo {
    top: 500px;
    background: var(--brand-blue);
    display: flex;
    align-items: center;
    justify-content: center;
  }
  .card--logo .card__wordmark {
    position: static;
    font-size: 104px;
    letter-spacing: 4px;
    color: var(--white);
    padding-bottom: 10px;
  }
</style>
</head>
<body>
<main class="canvas">

  <section class="card card--info" aria-label="Business card, contact side">
    <div class="ribbon">
      <svg width="350" height="66" viewBox="0 0 350 66" aria-hidden="true">
        <polygon points="0,0 350,0 322,33 350,66 0,66" fill="var(--brand-blue)"/>
      </svg>
    </div>
    <div class="holder">
      <p class="holder__name">Dale Fenwick</p>
      <p class="holder__title">President</p>
    </div>
    <ul class="contact">
      <li class="contact__item">
        <svg class="contact__icon" viewBox="0 0 18 18" aria-hidden="true">
          <path d="M4 1.5 L7 1.5 L8 5.5 L6 7 C7 9.5 8.5 11 11 12 L12.5 10 L16.5 11 L16.5 14 C16.5 15.5 15 16.5 13.5 16.5 C7 16 2 11 1.5 4.5 C1.5 3 2.5 1.5 4 1.5 Z" fill="var(--brand-blue)"/>
        </svg>
        <span>(800) 417-2964</span>
      </li>
      <li class="contact__item">
        <svg class="contact__icon" viewBox="0 0 18 18" aria-hidden="true">
          <rect x="1.5" y="3.5" width="15" height="11" rx="1.5" fill="none" stroke="var(--brand-blue)" stroke-width="1.8"/>
          <polyline points="2,4.5 9,10 16,4.5" fill="none" stroke="var(--brand-blue)" stroke-width="1.8"/>
        </svg>
        <span>sleep@quorvana.com</span>
      </li>
      <li class="contact__item">
        <svg class="contact__icon" viewBox="0 0 18 18" aria-hidden="true">
          <circle cx="9" cy="9" r="7.2" fill="none" stroke="var(--brand-blue)" stroke-width="1.7"/>
          <ellipse cx="9" cy="9" rx="3.2" ry="7.2" fill="none" stroke="var(--brand-blue)" stroke-width="1.4"/>
          <line x1="1.8" y1="9" x2="16.2" y2="9" stroke="var(--brand-blue)" stroke-width="1.4"/>
        </svg>
        <span>www.quorvana.com</span>
      </li>
    </ul>
    <p class="card__wordmark">quorvana</p>
    <div class="edge-tab" aria-hidden="true"></div>
  </section>

  <section class="card card--logo" aria-label="Business card, logo side">
    <p class="card__wordmark">quorvana</p>
  </section>

</main>
</body>
</html>
```